Locksmith Business Cards

My father-in-law is in need of new business cards for his locksmith business and I need to impress him. Kindly help me out!

You can see the previous business card attached. It is a family run business in the Glanfor Coast.

No individual names on the cards.

Key Things to Feature:
- The words "Prompt", "Local", "Reliable" (as you can see under the logo on the website)
- 24h Emergency Service
- Covering All of the Glanfor Coast, Penrhos Vale and Castellmor
- The color blue
- A key or a lock would be interesting (similar to the ones that come up when you google locksmith business card)

Optional (only if design includes bullet points, like the example below):
https://imgvaultcdnx.net/design_img/318264/57190/57190_2749031_318264_image.jpg
- Residential / Commercial / Automotive
- Alarms & Cameras
- Key Cutting & Safes

https://www.bryncoed-locksmiths-demo.co.uk/

Locksmith

01632 960 418
07700 900 362
bryncoedlocksmiths@mailvalex.com
Bryncoed Locksmiths, Hafod Barn, 4 Pennant Rd., Porthmelyn LL39 7QZ
www.bryncoed-locksmiths-demo.co.uk

• - The words "Prompt", "Local", "Reliable" (as you can see under the logo on the website)
• - 24h Emergency Service
• - Covering All of the Glanfor Coast, Penrhos Vale and Castellmor
• - A key or a lock would be interesting (similar to the ones that come up when you google locksmith business card)

```html
<!DOCTYPE html>
<html lang="en">
<head>
<meta charset="utf-8">
<title>Bryncoed Locksmiths – Business Cards</title>
<link rel="stylesheet" href="https://fonts.googleapis.com/css2?family=Oswald:wght@500&family=Open+Sans:ital,wght@0,400;0,600;0,700;1,600&display=swap">
<style>
  :root {
    --navy: #252a66;
    --navy-deep: #1f2360;
    --royal: #4a5aa8;
    --ink: #1e2258;
    --paper: #ffffff;
    --paper-shade: #f1f1f3;
    --backdrop: #2b2b2d;
    --grey-text: #dfe1ee;
  }
  * { box-sizing: border-box; margin: 0; padding: 0; }
  html, body { width: 1200px; height: 1021px; overflow: hidden; }
  body {
    background: var(--backdrop);
    font-family: "Open Sans", Arial, sans-serif;
    position: relative;
  }
  .card {
    position: absolute;
    left: 226px;
    width: 748px;
    height: 440px;
    border-radius: 3px;
    box-shadow: 0 10px 28px rgba(0,0,0,.45);
    overflow: hidden;
  }
  /* ---------- back ---------- */
  .card-back { top: 44px; background: var(--navy); color: #fff; }
  .back-brand {
    position: absolute; top: 130px; left: 0; right: 0;
    display: flex; align-items: center; justify-content: center; gap: 20px;
  }
  .brand-square { width: 70px; height: 70px; background: #fff; flex: none; }
  .brand-name {
    font-family: "Oswald", "Arial Narrow", sans-serif;
    font-weight: 500; font-size: 50px; line-height: 1; letter-spacing: 1px;
    text-transform: uppercase;
  }
  .back-services {
    position: absolute; top: 272px; left: 0; right: 0;
    text-align: center; font-size: 20px; line-height: 1.45; letter-spacing: .3px;
    color: var(--grey-text);
  }
  /* ---------- front ---------- */
  .card-front {
    top: 540px;
    background: linear-gradient(180deg, var(--paper) 55%, var(--paper-shade) 100%);
    color: var(--ink);
  }
  .front-identity { position: absolute; left: 40px; top: 62px; width: 310px; }
  .front-brand { display: flex; align-items: center; gap: 14px; }
  .front-brand .brand-square { width: 52px; height: 52px; background: var(--navy); }
  .front-brand .brand-name { font-size: 42px; color: var(--navy); line-height: 1.02; }
  .identity-rule { height: 2px; background: var(--royal); margin: 20px 0 16px; width: 280px; }
  .tagline { font-weight: 700; font-size: 25px; color: var(--ink); letter-spacing: .2px; }
  .emergency { font-weight: 600; font-size: 23px; color: var(--royal); letter-spacing: 1.5px; margin-top: 4px; }
  .front-contact {
    position: absolute; right: 36px; top: 52px; width: 384px;
    text-align: center; color: var(--ink);
  }
  .address { font-size: 18px; line-height: 1.35; }
  .phones { margin-top: 16px; }
  .phone {
    display: flex; align-items: center; justify-content: center; gap: 10px;
    font-weight: 700; font-size: 25px; line-height: 1.25; letter-spacing: .5px;
  }
  .phone svg { width: 20px; height: 22px; fill: var(--navy); flex: none; }
  .email { font-size: 17px; margin-top: 4px; }
  .website { font-size: 17px; font-weight: 700; color: var(--royal); margin-top: 14px; }
  .coverage { font-size: 19px; line-height: 1.3; margin-top: 22px; }
  .footer-band {
    position: absolute; left: 0; right: 0; bottom: 0; height: 26px; background: var(--navy-deep);
  }
  .footer-accent {
    position: absolute; left: 48px; bottom: 0; width: 270px; height: 26px;
    background: var(--royal); border-left: 4px solid #fff; border-right: 4px solid #fff;
  }
</style>
</head>
<body>
  <section class="card card-back" aria-label="Card back">
    <div class="back-brand">
      <span class="brand-square" aria-hidden="true"></span>
      <span class="brand-name">Bryncoed<br>Locksmiths</span>
    </div>
    <p class="back-services">
      Residential / Commercial / Automotive<br>
      Alarms &amp; Cameras&nbsp; | &nbsp;Key Cutting &amp; Safes
    </p>
  </section>

  <section class="card card-front" aria-label="Card front">
    <div class="front-identity">
      <div class="front-brand">
        <span class="brand-square" aria-hidden="true"></span>
        <span class="brand-name">Bryncoed<br>Locksmiths</span>
      </div>
      <div class="identity-rule"></div>
      <p class="tagline">Prompt. Local. Reliable</p>
      <p class="emergency">24h Emergency Service</p>
    </div>

    <div class="front-contact">
      <p class="address">Hafod Barn, 4 Pennant Rd.<br>Porthmelyn LL39 7QZ</p>
      <div class="phones">
        <p class="phone">
          <svg viewBox="0 0 24 24" aria-hidden="true"><path d="M6.6 10.8a15.1 15.1 0 0 0 6.6 6.6l2.2-2.2c.3-.3.7-.4 1-.2 1.1.4 2.3.6 3.6.6.6 0 1 .4 1 1V20c0 .6-.4 1-1 1A17 17 0 0 1 3 4c0-.6.4-1 1-1h3.5c.6 0 1 .4 1 1 0 1.3.2 2.5.6 3.6.1.3 0 .7-.2 1z"/></svg>
          01632 960 418
        </p>
        <p class="phone">
          <svg viewBox="0 0 24 24" aria-hidden="true"><path d="M7 1h10a2 2 0 0 1 2 2v18a2 2 0 0 1-2 2H7a2 2 0 0 1-2-2V3a2 2 0 0 1 2-2zm0 3v14h10V4zm5 15.5a1 1 0 1 0 0 2 1 1 0 0 0 0-2z"/></svg>
          07700 900 362
        </p>
      </div>
      <p class="email">bryncoedlocksmiths@mailvalex.com</p>
      <p class="website">www.bryncoed-locksmiths-demo.co.uk</p>
      <p class="coverage">Covering All of the Glanfor Coast,<br>Penrhos Vale and Castellmor</p>
    </div>

    <div class="footer-band"></div>
    <div class="footer-accent"></div>
  </section>
</body>
</html>
```